New Architectural Firm Business Cards

New Business card to compliment previous pixel forum logo (attached). Please design a business card that is simple, modern, creative....please do not use "symbols", simply the logo and associated graphics/text. The front should contain name/address/phone/email/web address (with graphics).....back should be 100% graphic design using the logo somehow. Hoping for a two color (black and yellow) design. full bleed design, no borders

Target Market(s)

Commercial Architecture Clients

Industry/Entity Type

Architecture

Contact Information for Business Card

Please design a business card that is simple, modern, creative....please do not use "symbols", simply the logo and associated graphics/text. The front should contain name/address/phone/email/web address (with graphics).....back should be 100% graphic design using the logo somehow

Font styles to use
Sans Serif

Colors
FFF300
FFF600
FEFA6F
FFFEC7
FFFEE8

Requirements
Must have
• Clean, Modern Design
Should not have
• Stock images or "icons"

```html
<!DOCTYPE html>
<html lang="en">
<head>
<meta charset="utf-8">
<title>Pixel Forum – Business Card</title>
<link href="https://fonts.googleapis.com/css2?family=Montserrat:wght@500;700;800&display=swap" rel="stylesheet">
<style>
  :root {
    --page-bg: #f0f0f1;
    --brand-yellow: #f7c511;
    --card-black: #000000;
    --card-white: #ffffff;
    --ink: #111111;
    --ink-soft: #3a3a3a;
    --rule: #555555;
    --faint-mark: #141414;
  }
  * { box-sizing: border-box; margin: 0; padding: 0; }
  html, body {
    width: 1200px; height: 2400px; overflow: hidden;
    background: var(--page-bg);
    font-family: "Montserrat", Arial, sans-serif;
  }
  .sheet {
    position: relative; width: 1200px; height: 2400px;
  }
  .card {
    position: absolute; left: 104px; width: 996px; height: 569px;
    overflow: hidden;
    box-shadow: 0 3px 6px rgba(0,0,0,0.25);
  }
  .card::before {
    content: ""; position: absolute; left: 0; top: 0; right: 0; height: 7px;
    background: var(--brand-yellow); z-index: 3;
  }
  .card--back { top: 609px; background: var(--card-black); }
  .card--front { top: 1222px; background: var(--card-white); }

  .back-watermark {
    position: absolute; left: 0; top: 110px; width: 485px; height: 459px;
    background: radial-gradient(ellipse at 60% 40%, var(--faint-mark) 0%, #0a0a0a 55%, var(--card-black) 100%);
  }
  .brand-name {
    position: absolute;
    color: var(--brand-yellow);
    font-weight: 800;
    letter-spacing: 0.02em;
    line-height: 0.95;
    text-transform: uppercase;
  }
  .card--back .brand-name {
    right: 74px; top: 368px; font-size: 64px; text-align: right;
  }

  .front-texture {
    position: absolute; inset: 0;
    background: linear-gradient(135deg, #f6f6f6 0%, #ffffff 45%, #f3f3f3 100%);
  }
  .card--front .brand-name {
    left: 124px; top: 215px; font-size: 58px; z-index: 2;
  }
  .divider {
    position: absolute; left: 486px; top: 95px; width: 1px; height: 419px;
    background: var(--rule); z-index: 2;
  }
  .identity { position: absolute; left: 545px; top: 126px; z-index: 2; }
  .identity__name {
    font-size: 49px; font-weight: 800; color: var(--ink); line-height: 1;
    letter-spacing: 0.01em;
  }
  .identity__name span { color: var(--brand-yellow); }
  .identity__role {
    margin-top: 14px; font-size: 21px; font-weight: 500; color: var(--ink-soft);
    letter-spacing: 0.03em;
  }
  .contacts {
    position: absolute; left: 545px; top: 284px; list-style: none; z-index: 2;
  }
  .contacts li {
    position: relative; padding-left: 41px;
    font-size: 24px; font-weight: 500; color: var(--ink-soft);
    letter-spacing: 0.03em; line-height: 30px; height: 30px;
  }
  .contacts li + li { margin-top: 20px; }
  .contacts li:last-child { margin-top: 24px; }
  .contacts li::before {
    content: ""; position: absolute; left: 2px; top: 9px;
    width: 12px; height: 12px; border-radius: 50%;
    background: var(--brand-yellow);
  }
  .contacts .contacts__phone { font-weight: 700; color: var(--ink); }
</style>
</head>
<body>
<main class="sheet">
  <section class="card card--back">
    <div class="back-watermark" role="img" aria-label="Large faint brand mark with hexagon texture"></div>
    <p class="brand-name">Pixel<br>Forum</p>
  </section>

  <section class="card card--front">
    <div class="front-texture" role="img" aria-label="Soft grey hexagon pattern background"></div>
    <p class="brand-name">Pixel<br>Forum</p>
    <div class="divider"></div>
    <div class="identity">
      <h1 class="identity__name">YOUR <span>NAME</span></h1>
      <p class="identity__role">Your Designation here</p>
    </div>
    <ul class="contacts">
      <li class="contacts__phone">123-456-7895</li>
      <li>Your address here</li>
      <li>your email address</li>
      <li>www.pixelforum-studio.com</li>
    </ul>
  </section>
</main>
</body>
</html>
```